Now Leasing Banner

Looking for a banner that says the following information approx 4' x 30'

Now Leasing Maplewood Terrace 925-318-6054

Target Market(s)

Drive by traffic

Industry/Entity Type

Residential property management

Requirements
Must have
• Clear and readable from a distance

```html
<!DOCTYPE html>
<html lang="en">
<head>
<meta charset="utf-8">
<title>Maplewood Terrace – Now Leasing Banner</title>
<link rel="stylesheet" href="https://fonts.googleapis.com/css2?family=Great+Vibes&family=Oswald:wght@600&family=Bebas+Neue&display=swap">
<style>
  :root {
    --page: #ffffff;
    --forest: #36574a;
    --cream: #ffffff;
    --bronze: #6b4a22;
    --panel-top: #e8e8e0;
    --panel-bottom: #c6d3b4;
    --sepia-light: #ddd3c0;
    --sepia-dark: #8a6c3c;
    --edge: #c9c9c9;
  }
  html, body {
    margin: 0;
    width: 1200px;
    height: 325px;
    overflow: hidden;
    background: var(--page);
  }
  .banner {
    position: absolute;
    left: 41px;
    top: 87px;
    width: 1125px;
    height: 151px;
    background: var(--forest);
    box-shadow: 0 0 0 1px var(--edge);
    overflow: hidden;
  }
  .community-art {
    position: absolute;
    left: 0;
    top: 0;
    width: 251px;
    height: 151px;
    background: linear-gradient(180deg, var(--sepia-light) 0%, #c2ad88 55%, var(--sepia-dark) 100%);
  }
  .banner-text {
    position: absolute;
    left: 0;
    top: 0;
    width: 1125px;
    height: 151px;
  }
  .property-name {
    font-family: "Great Vibes", cursive;
    fill: var(--cream);
    filter: drop-shadow(0 0 1.5px rgba(0,0,0,0.6));
  }
  .leasing-headline {
    font-family: "Oswald", sans-serif;
    font-weight: 600;
    fill: var(--cream);
  }
  .phone-number {
    font-family: "Bebas Neue", sans-serif;
    fill: var(--bronze);
  }
</style>
</head>
<body>
  <div class="banner">
    <div class="community-art" role="img" aria-label="Sepia illustration of the townhome community with trees and a picket fence"></div>
    <svg class="banner-text" viewBox="0 0 1125 151" width="1125" height="151" aria-label="Maplewood Terrace, now leasing, 925.318.6054">
      <defs>
        <linearGradient id="phone-panel-fill" x1="0" y1="0" x2="0" y2="1">
          <stop offset="0" stop-color="var(--panel-top)"/>
          <stop offset="0.6" stop-color="#dfe2d3"/>
          <stop offset="1" stop-color="var(--panel-bottom)"/>
        </linearGradient>
      </defs>
      <text class="property-name" x="272" y="73" font-size="74" textLength="330" lengthAdjust="spacingAndGlyphs">Maplewood</text>
      <text class="property-name" x="392" y="132" font-size="70" textLength="220" lengthAdjust="spacingAndGlyphs">Terrace</text>

      <text class="leasing-headline" x="657" y="69" font-size="72" textLength="436" lengthAdjust="spacingAndGlyphs">NOW LEASING</text>

      <rect class="phone-panel" x="658" y="76" width="436" height="75" fill="url(#phone-panel-fill)"/>
      <text class="phone-number" x="674" y="138" font-size="74" textLength="410" lengthAdjust="spacingAndGlyphs">925.318.6054</text>
    </svg>
  </div>
</body>
</html>
```